Quillfield HVAC WordPress website design

Design a new modern, clean, website for HVAC mechanical business that uses company logo/colors for branding and recognition. Files attached are just for band and color information. Here is a website design that appeals to me https://www.kestwellpartners.com/

A clear description of who we are and what we do

An easily-navigated site map

An easily-navigated site map for mobile devices

Easy-to-find contact information

Obvious call to action for service, installs or to schedule estimates

about us page

Provide a way for potential customers to contact us via text or email

provide a way that allows a customer to upload a picture to request a service call or quote.

I'm looking for the design to be completed in WordPress

Industry/Entity Type

HVAC Mechanical & Building Automation / Controls contractor

Coding

Coded - Design and coding required

Number of Pages Required

5+ page

Colors
0054AA
0677BA
7BADD7
CADEEF
E8F1F8

Requirements
Must have
• Design a new modern, clean, website for HVAC mechanical business that uses company logo/colors for branding and recognition. Files attached are just for band and color information. Here is a website design that appeals to me https://www.kestwellpartners.com/ A clear description of who we are and what we do An easily-navigated site map An easily-navigated site map for mobile devices Easy-to-find contact information Obvious call to action for service, installs or to schedule estimates about us page Provide a way for potential customers to contact us via text or email provide a way that allows a customer to upload a picture to request a service call or quote.
Nice to have

```html
<!DOCTYPE html>
<html lang="en">
<head>
<meta charset="utf-8">
<title>Quillfield HVAC</title>
<link href="https://fonts.googleapis.com/css2?family=Montserrat:wght@400;500;600&family=Playfair+Display:wght@800;900&display=swap" rel="stylesheet">
<style>
:root{
  --navy:#0b1f5e;
  --navy-deep:#081a52;
  --blue:#0054aa;
  --blue-mid:#0677ba;
  --sky:#7badd7;
  --pale:#e3e9fb;
  --card:#efefef;
  --text:#333;
  --white:#fff;
  --star:#f5b400;
}
*{box-sizing:border-box;margin:0;padding:0}
html,body{width:1200px;height:3076px;overflow:hidden}
body{position:relative;background:var(--white);font-family:"Montserrat",sans-serif;color:var(--text)}
.abs{position:absolute}
.serif{font-family:"Playfair Display",serif;font-weight:900;color:var(--navy);text-transform:uppercase}

.topbar{left:0;top:0;width:1200px;height:57px;background:var(--navy)}
.topbar .item{top:18px;color:var(--white);font-size:16px;font-weight:500;display:flex;align-items:center;gap:14px}
.header{left:0;top:57px;width:1200px;height:107px;background:var(--white)}
.brand{left:124px;top:90px;display:flex;align-items:center;gap:10px;font-family:"Montserrat",sans-serif;font-weight:600;font-size:20px;color:var(--navy);white-space:nowrap}
.brand .dot{width:34px;height:34px;border-radius:50%;background:var(--navy)}
.nav a{position:absolute;top:102px;font-size:16px;font-weight:500;color:#111;text-decoration:none}

.btn{position:absolute;display:flex;align-items:center;background:var(--navy);color:var(--white);font-weight:600;overflow:hidden;white-space:nowrap}
.btn .arrow{position:absolute;right:0;top:0;height:100%;background:var(--blue);clip-path:polygon(14px 0,100% 0,100% 100%,0 100%);display:flex;align-items:center;justify-content:center}
.btn.outline{background:transparent;border:1px solid var(--white)}

.hero{left:0;top:164px;width:1200px;height:514px;background:linear-gradient(90deg,#b9b9bb 0%,#cfcfd1 45%,#bdbdbf 100%)}
.form{left:774px;top:234px;width:396px;height:480px;background:var(--white);border-radius:6px;box-shadow:0 2px 12px rgba(0,0,0,.15)}
.form h2{position:absolute;left:0;top:16px;width:100%;text-align:center;font-size:24px}
.field{position:absolute;border:1px solid #e3e3e3;border-radius:3px;font-size:11.5px;font-weight:500;color:#222;padding:12px 9px;text-transform:uppercase}
.van{left:786px;top:626px;width:370px;height:150px;border-radius:24px;background:linear-gradient(180deg,#e9eaee 0%,#c9ccd3 100%)}

.services{left:111px;top:837px;width:978px;height:324px;border:1px solid #cfcfd6;display:flex}
.svc{flex:1;padding:38px 30px 0;border-right:1px solid #cfcfd6}
.svc:last-child{border-right:0}
.svc.active{background:var(--pale)}
.svc h3{font-size:21px;margin-bottom:14px;white-space:nowrap}
.svc p{font-size:15.5px;line-height:31px;width:265px}
.svc svg{margin-top:28px}

.band{left:0;top:1655px;width:1200px;height:513px;background:linear-gradient(135deg,var(--navy-deep),#0d2468 50%,var(--navy-deep))}
.about-img{left:177px;top:1313px;width:354px;height:440px;background:linear-gradient(180deg,#b7aca1,#c9bfb4 50%,#a39686)}
.about{left:531px;top:1313px;width:492px;height:440px;background:var(--white);box-shadow:0 2px 8px rgba(0,0,0,.08);padding:34px 55px}
.about h2{font-size:32px;margin-bottom:18px}
.about p{font-size:15.5px;line-height:31px}

.dark h2{color:var(--white)}
.dark p{color:var(--white);font-size:16px;line-height:31px}

.tcard{top:2334px;width:313px;height:266px;background:var(--card);padding:32px 28px}
.tcard .avatar{position:absolute;left:28px;top:32px;width:58px;height:58px;border-radius:50%;background:linear-gradient(160deg,#d8c3b0,#8a7a70)}
.tcard .name{position:absolute;left:111px;top:36px;color:var(--navy);font-size:18px;font-weight:500}
.tcard .date{position:absolute;left:111px;top:64px;font-size:16px;font-weight:500}
.tcard .stars{position:absolute;left:27px;top:112px;display:flex;gap:6px}
.tcard p{position:absolute;left:27px;top:148px;width:265px;font-size:16px;line-height:31px;color:#222}

.footer{left:0;top:2686px;width:1200px;height:390px;background:var(--navy)}
.footer .brand{position:absolute;left:0;width:1200px;top:94px;justify-content:center;color:var(--white);font-size:24px}
.footer .brand .dot{background:var(--white)}
.fnav a{position:absolute;top:214px;color:var(--white);font-size:16.5px;font-weight:500;text-decoration:none}
.social{position:absolute;top:262px;width:34px;height:34px;border:1.5px solid var(--white);border-radius:50%}
.copy{position:absolute;top:323px;width:1200px;text-align:center;color:var(--white);font-size:16px;font-weight:500}
</style>
</head>
<body>

<div class="abs topbar">
  <div class="abs item" style="left:510px">
    <svg width="16" height="16" viewBox="0 0 24 24"><path fill="#fff" d="M6.6 10.8a15 15 0 0 0 6.6 6.6l2.2-2.2c.3-.3.7-.4 1-.2 1.1.4 2.3.6 3.6.6.6 0 1 .4 1 1V20c0 .6-.4 1-1 1A17 17 0 0 1 3 4c0-.6.4-1 1-1h3.5c.6 0 1 .4 1 1 0 1.3.2 2.5.6 3.6.1.3 0 .7-.2 1z"/></svg>
    603-555-0142
  </div>
  <div class="abs item" style="left:744px">
    <svg width="18" height="14" viewBox="0 0 18 14"><rect width="18" height="14" fill="#fff"/><path d="M1 1l8 6 8-6" stroke="#0b1f5e" stroke-width="1.5" fill="none"/></svg>
    INFO@QUILLFIELDHVAC.NET
  </div>
  <svg class="abs" style="left:1069px;top:20px" width="17" height="17" viewBox="0 0 17 17"><circle cx="7" cy="7" r="5.5" stroke="#fff" stroke-width="1.8" fill="none"/><path d="M11 11l5 5" stroke="#fff" stroke-width="1.8"/></svg>
</div>

<div class="abs header"></div>
<div class="abs brand"><span class="dot"></span>Quillfield HVAC</div>
<nav class="nav">
  <a style="left:381px">HOME</a>
  <a style="left:469px">WHO WE ARE</a>
  <a style="left:621px">WHAT WE DO</a>
  <a style="left:772px">CONTACT US</a>
</nav>
<div class="btn" style="left:918px;top:86px;width:212px;height:48px;padding-left:18px;font-size:15.5px">SCHEDULE NOW
  <span class="arrow" style="width:54px"><svg width="9" height="14" viewBox="0 0 9 14"><path d="M2 2l5 5-5 5" stroke="#fff" stroke-width="1.8" fill="none"/></svg></span>
</div>

<div class="abs hero" role="img" aria-label="Couple using a remote to adjust a wall-mounted air conditioner"></div>

<div class="abs form">
  <h2 class="serif">Request a Service Call</h2>
  <div class="field" style="left:13px;top:72px;width:184px">First Name</div>
  <div class="field" style="left:200px;top:72px;width:184px">Last Name</div>
  <div class="field" style="left:13px;top:124px;width:184px">Email Address</div>
  <div class="field" style="left:200px;top:124px;width:184px">Mobile Number</div>
  <div class="field" style="left:13px;top:176px;width:371px">Upload Pictures</div>
  <div class="field" style="left:13px;top:229px;width:371px;height:92px">Type Your Message</div>
  <div class="btn" style="left:105px;top:339px;width:186px;height:42px;padding-left:13px;font-size:15.5px">SUBMIT HERE
    <span class="arrow" style="width:48px"><svg width="9" height="14" viewBox="0 0 9 14"><path d="M2 2l5 5-5 5" stroke="#fff" stroke-width="1.8" fill="none"/></svg></span>
  </div>
</div>
<div class="abs van" role="img" aria-label="Company service van"></div>

<h2 class="abs serif" style="left:112px;top:757px;font-size:32px">What We Do</h2>
<div class="abs services">
  <div class="svc">
    <h3 class="serif">Air Conditioning</h3>
    <p>Sed ut perspiciatis unde omnis iste natus error sit voluptatem accusantium doloremque laudantium, totam rem....</p>
    <svg width="84" height="70" viewBox="0 0 84 70" fill="none" stroke="#0b1f5e" stroke-width="2.5"><rect x="2" y="2" width="80" height="30" rx="3"/><path d="M30 12h46M30 18h46M30 24h46"/><circle cx="22" cy="46" r="20" fill="#fff"/><path d="M22 30v32M8 38l28 16M8 54l28-16"/><path d="M50 48c-4 4 4 8 0 12M58 48c-4 4 4 8 0 12M66 48c-4 4 4 8 0 12"/></svg>
  </div>
  <div class="svc active">
    <h3 class="serif">Heating</h3>
    <p>Sed ut perspiciatis unde omnis iste natus error sit voluptatem accusantium doloremque laudantium, totam rem....</p>
    <svg width="72" height="70" viewBox="0 0 72 70" fill="none" stroke="#0b1f5e" stroke-width="2.5"><path d="M38 6a7 7 0 0 1 14 0v40a12 12 0 1 1-14 0z"/><circle cx="45" cy="56" r="5"/><path d="M45 50V22M56 12h8M56 20h6M56 28h8M56 36h6"/><circle cx="17" cy="24" r="7"/><path d="M17 10v-5M17 43v-5M3 24H0M34 24h-3M7 14l-3-3M27 34l3 3M7 34l-3 3M27 14l3-3"/></svg>
  </div>
  <div class="svc">
    <h3 class="serif">Heat Pumps/Gas/Oil</h3>
    <p>Sed ut perspiciatis unde omnis iste natus error sit voluptatem accusantium doloremque laudantium, totam rem....</p>
    <svg width="74" height="70" viewBox="0 0 74 70" fill="none" stroke="#0b1f5e" stroke-width="2.5"><rect x="40" y="2" width="20" height="10" rx="2"/><path d="M6 14v48M16 14v48M26 14v48M36 14v48M46 14v48M56 14v48M66 14v48M2 22h70M2 52h70M10 62v6M62 62v6"/></svg>
  </div>
</div>

<svg class="abs" style="left:530px;top:1201px" width="140" height="26" viewBox="0 0 140 26"><circle cx="13" cy="13" r="12.5" fill="#0b1f5e"/><path d="M15 8l-5 5 5 5" stroke="#fff" stroke-width="2" fill="none"/><circle cx="42" cy="13" r="3.5" stroke="#0b1f5e" fill="none"/><circle cx="70" cy="13" r="3.5" stroke="#0b1f5e" fill="none"/><circle cx="98" cy="13" r="3.5" stroke="#0b1f5e" fill="none"/><circle cx="127" cy="13" r="12.5" fill="#0b1f5e"/><path d="M125 8l5 5-5 5" stroke="#fff" stroke-width="2" fill="none"/></svg>

<div class="abs band"></div>
<div class="abs about-img" role="img" aria-label="Family relaxing on a sofa under a cooling air conditioner"></div>
<div class="abs about">
  <h2 class="serif">Who We Are</h2>
  <p>Lorem ipsum dolor sit amet, consectetur adipiscing elit, sed do eiusmod tempor incididunt ut labore et dolore magna aliqua. Ut enim ad minim veniam, quis nostrud exercitation ullamco laboris nisi ut aliquip ex ea commodo consequat. Duis aute irure dolor in reprehenderit in voluptate velit esse cillum dolore eu fugiat nulla pariatur.</p>
  <div class="btn" style="left:55px;top:359px;width:186px;height:42px;padding-left:14px;font-size:15.5px">LEARN MORE
    <span class="arrow" style="width:48px"><svg width="9" height="14" viewBox="0 0 9 14"><path d="M2 2l5 5-5 5" stroke="#fff" stroke-width="1.8" fill="none"/></svg></span>
  </div>
</div>

<div class="abs dark" style="left:178px;top:1826px;width:380px">
  <h2 class="serif" style="font-size:32px;margin-bottom:16px">Ask Question</h2>
  <p>Lorem ipsum dolor sit amet, consectetur adipiscing elit, sed do eiusmod tempor</p>
</div>
<div class="btn outline" style="left:179px;top:1970px;width:290px;height:42px;padding-left:14px;font-size:15.5px;font-weight:500">LOOK PREVIOUS QUESTIONS
  <span class="arrow" style="width:48px"><svg width="9" height="14" viewBox="0 0 9 14"><path d="M2 2l5 5-5 5" stroke="#fff" stroke-width="1.8" fill="none"/></svg></span>
</div>
<div class="abs" style="left:599px;top:1803px;width:1px;height:310px;background:rgba(255,255,255,.4)"></div>
<div class="abs dark" style="left:652px;top:1826px;width:360px">
  <h2 class="serif" style="font-size:32px;margin-bottom:16px">FAQ</h2>
  <p style="margin-bottom:6px">1. Lorem ipsum dolor sit amet ?</p>
  <p>Lorem ipsum dolor sit amet, consectetur adipiscing elit, sed do eiusmod tempor</p>
  <p style="font-family:'Playfair Display',serif;font-weight:800;margin-top:12px;font-size:15px">JAN 23 | JOHN</p>
</div>
<svg class="abs" style="left:652px;top:2053px" width="78" height="26" viewBox="0 0 78 26"><circle cx="13" cy="13" r="12.5" fill="#fff"/><path d="M15 8l-5 5 5 5" stroke="#0b1f5e" stroke-width="2" fill="none"/><circle cx="65" cy="13" r="12.5" fill="#fff"/><path d="M63 8l5 5-5 5" stroke="#0b1f5e" stroke-width="2" fill="none"/></svg>

<h2 class="abs serif" style="left:112px;top:2245px;font-size:32px">What Our Customer Says</h2>
<svg class="abs" style="left:1034px;top:2254px" width="58" height="22" viewBox="0 0 58 22"><path d="M10 3l-7 8 7 8" stroke="#0b1f5e" stroke-width="2.4" fill="none"/><path d="M48 3l7 8-7 8" stroke="#0b1f5e" stroke-width="2.4" fill="none"/></svg>

<div class="abs tcard" style="left:111px">
  <div class="avatar" role="img" aria-label="Customer portrait"></div>
  <div class="name">LOREM IPSUM</div><div class="date">JAN 2, 2024</div>
  <div class="stars"><svg width="110" height="16" viewBox="0 0 110 16"><g fill="#f5b400"><path id="s" d="M8 0l2.4 5 5.6.6-4.2 3.8 1.2 5.6L8 12.2 3 15l1.2-5.6L0 5.6 5.6 5z"/><use href="#s" x="22"/><use href="#s" x="44"/><use href="#s" x="66"/><use href="#s" x="88"/></g></svg></div>
  <p>Lorem ipsum dolor sit amet, consectetur adipiscing elit, sed do eiusmod tempor</p>
</div>
<div class="abs tcard" style="left:444px">
  <div class="avatar" role="img" aria-label="Customer portrait"></div>
  <div class="name">LOREM IPSUM</div><div class="date">JAN 2, 2024</div>
  <div class="stars"><svg width="110" height="16" viewBox="0 0 110 16"><g fill="#f5b400"><use href="#s"/><use href="#s" x="22"/><use href="#s" x="44"/><use href="#s" x="66"/><use href="#s" x="88"/></g></svg></div>
  <p>Lorem ipsum dolor sit amet, consectetur adipiscing elit, sed do eiusmod tempor</p>
</div>
<div class="abs tcard" style="left:776px">
  <div class="avatar" role="img" aria-label="Customer portrait"></div>
  <div class="name">LOREM IPSUM</div><div class="date">JAN 2, 2024</div>
  <div class="stars"><svg width="110" height="16" viewBox="0 0 110 16"><g fill="#f5b400"><use href="#s"/><use href="#s" x="22"/><use href="#s" x="44"/><use href="#s" x="66"/><use href="#s" x="88"/></g></svg></div>
  <p>Lorem ipsum dolor sit amet, consectetur adipiscing elit, sed do eiusmod tempor</p>
</div>

<footer class="abs footer">
  <div class="brand"><span class="dot"></span>Quillfield HVAC</div>
  <nav class="fnav">
    <a style="left:350px">HOME</a>
    <a style="left:439px">WHO WE ARE</a>
    <a style="left:591px">WHAT WE DO</a>
    <a style="left:743px">CONTACT US</a>
  </nav>
  <span class="social" style="left:543px"></span>
  <span class="social" style="left:583px"></span>
  <span class="social" style="left:623px"></span>
  <div class="copy">@2024 COPYRIGHTS . ALL RIGHTS RESERVED</div>
</footer>

</body>
</html>
```